Custom Real Estate Flyer

Hi, I'm looking for a classy custom flyer to market residential homes listed for sale in Southern California. I've uploaded my logo's and I'd like to incorporate the logo's into my flyer for branding. I"d like something classy that really showcases pictures of the home for sale. Thank you so much!

8 1/2 x 11 sized page, either one or two sided with maybe logo on back like business card :)
Updates

Thank you everyone! I appreciate your designs very much! :) Please continue to submit.

Target Market(s)

This flyer will showcase my listings and potential clients will see it in my open houses. Hoping for something original and that is memorable :)

Industry/Entity Type

Residential

Requirements
Must have
• **ALL INFO AND LOGO'S ON MY BUSINESS CARD MUST BE ON THE FLYER** (legal requirements), also I want to be able to edit the text and change the pictures on the flyer for all of my listings :)

The word HOMEBROKER must be in all caps and have the "R" in the circle (please refer to business card)

Must have my license number: CalBRE #04729158 (no changes, please refer to business card)

My logo should remain the same.

Please use the Homestead Partners logo submitted.

Nice to have
• I like a fade in the background, and borders around the house pictures.

I'd like a bullet point section and a paragraph section if possible :)

Should not have
• Flyer does not need a mobile scan code.

I don't care for slanted or cut off photo's of the home.

```html
<!DOCTYPE html>
<html lang="en">
<head>
<meta charset="utf-8">
<title>Listing Flyer – Dana Whitfield</title>
<link rel="stylesheet" href="https://fonts.googleapis.com/css2?family=Bebas+Neue&family=Oswald:wght@500&family=Roboto+Condensed:wght@400&family=Arimo:wght@400;700&display=swap">
<style>
  :root {
    --navy: #174785;
    --band: #1d55a6;
    --card-blue: #4f80c4;
    --heading-blue: #1b4a8c;
    --body-grey: #3c3c3c;
    --paper-top: #e6e6e6;
    --paper-bottom: #fbfbfb;
  }
  * { margin: 0; padding: 0; box-sizing: border-box; }
  html, body { width: 928px; height: 1200px; overflow: hidden; background: #ffffff; }
  .flyer {
    position: relative; width: 928px; height: 1200px; overflow: hidden;
    background: linear-gradient(180deg, var(--paper-top) 0, #f2f2f2 420px, var(--paper-bottom) 1150px);
  }
  .hero-panel {
    position: absolute; left: 0; top: 0; width: 456px; height: 336px; background: var(--navy);
  }
  .hero-title {
    position: absolute; left: 44px; top: 66px;
    font-family: "Bebas Neue", "Oswald", sans-serif; font-weight: 400;
    font-size: 66px; line-height: 64px; color: #ffffff; letter-spacing: 0.5px;
    text-shadow: 0 0 8px #6fa8ff, 0 0 3px #9cc4ff;
  }
  .hero-photo {
    position: absolute; left: 467px; top: 0; width: 461px; height: 336px;
    background: linear-gradient(160deg, #f4f1ec 0%, #d9b48c 38%, #b9876a 55%, #8a8d83 78%, #d8d2c8 100%);
  }
  .hero-shadow {
    position: absolute; left: 0; top: 336px; width: 928px; height: 20px;
    background: linear-gradient(180deg, rgba(0,0,0,0.10), rgba(0,0,0,0));
  }
  .listing { position: absolute; width: 274px; }
  .listing-photo { width: 274px; height: 180px; border-radius: 12px; }
  .listing-title {
    margin-top: 12px;
    font-family: "Oswald", sans-serif; font-weight: 500; font-size: 16px; line-height: 18px;
    color: var(--heading-blue); text-transform: uppercase; letter-spacing: 0.1px;
  }
  .listing-text {
    margin-top: 2px;
    font-family: "Roboto Condensed", sans-serif; font-size: 8.6px; line-height: 10.2px;
    color: var(--body-grey); text-align: justify;
  }
  .tone-exterior { background: linear-gradient(170deg, #dfe9f5 0%, #f1eee8 35%, #c6c1b4 55%, #5f9a3a 72%, #4f8a2e 100%); }
  .tone-bedroom { background: linear-gradient(180deg, #b9b6ae 0%, #cfcbc2 45%, #ece9e2 70%, #d6cfc2 100%); }
  .tone-living { background: linear-gradient(180deg, #e9e8e4 0%, #d8d6d0 45%, #a2604f 62%, #8b8275 100%); }
  .tone-lounge { background: linear-gradient(180deg, #efefec 0%, #dedbd5 45%, #6b5a48 65%, #8c8478 100%); }
  .tone-dining { background: linear-gradient(180deg, #e8ebe8 0%, #cfd5cc 45%, #5a4c42 62%, #c08a52 100%); }
  .tone-stairs { background: linear-gradient(180deg, #ecebe6 0%, #d5d1c8 45%, #5f4d44 62%, #b7a994 100%); }
  .footer-band {
    position: absolute; left: 0; top: 1152px; width: 928px; height: 48px; background: var(--band);
  }
  .agent-card {
    position: absolute; left: 460px; top: 944px; width: 398px; height: 242px;
    display: flex; box-shadow: 0 2px 6px rgba(0,0,0,0.25);
  }
  .agent-portrait {
    width: 163px; height: 242px;
    background: linear-gradient(180deg, #bdbdbd 0%, #8d8d8d 55%, #2a2a2a 100%);
  }
  .agent-details {
    position: relative; flex: 1; background: var(--card-blue); color: #ffffff;
    font-family: "Arimo", sans-serif;
  }
  .brokerage {
    position: absolute; left: 22px; top: 30px; width: 90px; text-align: center;
    font-size: 10px; font-weight: 700; line-height: 12px;
  }
  .brokerage-mark {
    display: block; width: 14px; height: 14px; margin: 0 auto 5px; background: #ffffff;
  }
  .brokerage-area { display: block; margin-top: 12px; font-size: 8.5px; font-weight: 400; }
  .agent-name {
    position: absolute; right: 32px; top: 70px; text-align: center; width: 110px;
  }
  .agent-name strong { display: block; font-size: 12px; font-weight: 700; line-height: 14px; }
  .agent-name span { display: block; font-size: 8.5px; line-height: 11px; }
  .contact {
    position: absolute; right: 32px; top: 96px; text-align: right; line-height: 14.5px;
  }
  .license { font-size: 7px; line-height: 10px; margin-bottom: 14px; }
  .address { font-size: 11px; line-height: 14.5px; }
  .phones { font-size: 11.5px; font-weight: 700; margin-top: 4px; line-height: 15px; }
  .web { font-size: 11.5px; font-weight: 700; margin-top: 12px; line-height: 15px; }
</style>
</head>
<body>
<div class="flyer">
  <section class="hero-panel">
    <h1 class="hero-title">We can help you<br>to realize your<br>greatest dream</h1>
  </section>
  <div class="hero-photo" role="img" aria-label="Photo of a couple embracing in front of a modern two-storey home"></div>
  <div class="hero-shadow"></div>

  <article class="listing" style="left:46px; top:382px;">
    <div class="listing-photo tone-exterior" role="img" aria-label="Front exterior of the listed home with lawn and garage"></div>
    <h2 class="listing-title">Lorem ipsum dolor sit amet</h2>
    <p class="listing-text">consectetur adipiscing elit. Morbi malesuada diam est, integer odio erat, lacinia elementum orci id, fermentum fermentum felis. Nullam vitae massa rutrum, bibendum mi a, ornare orci. Nunc sodales diam a lorem ornare, sed lobortis diam eleifend. Vivamus ac porttitor nunc, eu auctor tortor.</p>
  </article>
  <article class="listing" style="left:338px; top:382px;">
    <div class="listing-photo tone-bedroom" role="img" aria-label="Master bedroom with made bed"></div>
    <h2 class="listing-title">Lorem ipsum dolor sit amet</h2>
    <p class="listing-text">consectetur adipiscing elit. Morbi malesuada diam est, integer odio erat, lacinia elementum orci id, fermentum fermentum felis. Nullam vitae massa rutrum, bibendum mi a, ornare orci. Nunc sodales diam a lorem ornare, sed lobortis diam eleifend. Vivamus ac porttitor nunc, eu auctor tortor.</p>
  </article>
  <article class="listing" style="left:630px; top:382px;">
    <div class="listing-photo tone-living" role="img" aria-label="Family room with brick fireplace"></div>
    <h2 class="listing-title">Lorem ipsum dolor sit amet</h2>
    <p class="listing-text">consectetur adipiscing elit. Morbi malesuada diam est, integer odio erat, lacinia elementum orci id, fermentum fermentum felis. Nullam vitae massa rutrum, bibendum mi a, ornare orci. Nunc sodales diam a lorem ornare, sed lobortis diam eleifend. Vivamus ac porttitor nunc, eu auctor tortor.</p>
  </article>

  <article class="listing" style="left:46px; top:655px;">
    <div class="listing-photo tone-lounge" role="img" aria-label="Living room with sofa, armchair and coffee table"></div>
    <h2 class="listing-title">Lorem ipsum dolor sit amet</h2>
    <p class="listing-text">consectetur adipiscing elit. Morbi malesuada diam est, integer odio erat, lacinia elementum orci id, fermentum fermentum felis. Nullam vitae massa rutrum, bibendum mi a, ornare orci. Nunc sodales diam a lorem ornare, sed lobortis diam eleifend. Vivamus ac porttitor nunc, eu auctor tortor.</p>
  </article>
  <article class="listing" style="left:338px; top:655px;">
    <div class="listing-photo tone-dining" role="img" aria-label="Dining area with table and wood floors"></div>
    <h2 class="listing-title">Lorem ipsum dolor sit amet</h2>
    <p class="listing-text">consectetur adipiscing elit. Morbi malesuada diam est, integer odio erat, lacinia elementum orci id, fermentum fermentum felis. Nullam vitae massa rutrum, bibendum mi a, ornare orci. Nunc sodales diam a lorem ornare, sed lobortis diam eleifend. Vivamus ac porttitor nunc, eu auctor tortor.</p>
  </article>
  <article class="listing" style="left:630px; top:655px;">
    <div class="listing-photo tone-stairs" role="img" aria-label="Entry hall with carpeted staircase"></div>
    <h2 class="listing-title">Lorem ipsum dolor sit amet</h2>
    <p class="listing-text">consectetur adipiscing elit. Morbi malesuada diam est, integer odio erat, lacinia elementum orci id, fermentum fermentum felis. Nullam vitae massa rutrum, bibendum mi a, ornare orci. Nunc sodales diam a lorem ornare, sed lobortis diam eleifend. Vivamus ac porttitor nunc, eu auctor tortor.</p>
  </article>

  <article class="listing" style="left:46px; top:934px;">
    <div class="listing-photo tone-exterior" role="img" aria-label="Front exterior of the listed home with lawn and garage"></div>
    <h2 class="listing-title">Lorem ipsum dolor sit amet</h2>
  </article>

  <div class="footer-band"></div>

  <aside class="agent-card">
    <div class="agent-portrait" role="img" aria-label="Black and white portrait of the agent"></div>
    <div class="agent-details">
      <div class="brokerage">
        <span class="brokerage-mark"></span>
        Homestead Partners
        <span class="brokerage-area">CEDAR HOLLOW</span>
      </div>
      <div class="agent-name">
        <strong>Dana Whitfield</strong>
        <span>HOMEBROKER®</span>
      </div>
      <div class="contact">
        <p class="license">CalBRE #04729158</p>
        <p class="address">18420 Orchard Lane<br>Cedar Hollow, CA 91400</p>
        <p class="phones">555.204.3817 (Cell)<br>555.318.4400 VM 2716 (Office)</p>
        <p class="web">www.DanaWhitfield.com<br>Dana@DanaWhitfield.com</p>
      </div>
    </div>
  </aside>
</div>
</body>
</html>
```